Falcon KOR-VEN (Salabat and Turmeric) Health Drink 100 grams

We need a packaging design for this product. Attached is the packaging size, including the folds. indicated also are the front and back portions of the package. I have attached the following files:
1. "FALCON" logo - from the refined sugar layout
2. layout of the packaging
3. Owl Crest layout - so you will have an idea of how the product will look like
4. Health Benefits of Ginger and Turmeric - this should be written at the back portion

Ingredients: White Sugar, Ginger and Turmeric
Size: 100 grams
Preparation: 1. Pour 1 teaspoon of KORVEN into a cup of hot water. 2. Stir well and enjoy!

Company Name: FALCON READY MEAL COMMERCE
Address: JM Velasco St., Hillcrest, Tabuyan, Lunaria City

Leave space for the barcode.

Just use your imagination. We are very particular with regards to the look of the front.

Target Market(s)

ALL CLASSES. MUST ATTRACT CLASS A MARKET

Industry/Entity Type

Health

Requirements
Must have
• HEALTH BENEFITS, SERVING INSTRUCTIONS,
Nice to have
• A SEE-THROUGH WINDOW ON THE FRONT PORTION SO THAT THE CUSTOMER CAN SEE THE PRODUCT
Should not have
• OPEN

```html
<!DOCTYPE html>
<html lang="en">
<head>
<meta charset="utf-8">
<title>Falcon KOR-VEN Ginger + Turmeric Pouch</title>
<link href="https://fonts.googleapis.com/css2?family=Oswald:wght@300;400;500;700&family=Roboto:wght@400;700&display=swap" rel="stylesheet">
<style>
  :root {
    --bg: #e6e6e6;
    --pouch: #2b2927;
    --seal: #242220;
    --fold: #33302d;
    --gold: #c9962f;
    --gold-light: #e0b35a;
    --powder-a: #e6a72a;
    --powder-b: #c98a18;
    --ink: #232120;
    --label-white: #f1f1f1;
  }
  * { box-sizing: border-box; margin: 0; padding: 0; }
  html, body { width: 1200px; height: 917px; overflow: hidden; }
  body {
    background: var(--bg);
    position: relative;
    font-family: "Oswald", sans-serif;
    color: var(--gold);
  }
  .pouch {
    position: absolute;
    top: 112px;
    width: 452px;
    height: 680px;
    background: var(--pouch);
  }
  .pouch--front { left: 88px; }
  .pouch--back { left: 620px; }
  .seal {
    position: absolute;
    left: 0; right: 0;
    height: 44px;
    background: var(--seal);
  }
  .seal--top { top: 0; }
  .seal--bottom { bottom: 0; }

  /* Front */
  .claim {
    position: absolute;
    top: 70px; left: 0; right: 0;
    text-align: center;
    font-size: 27px;
    font-weight: 400;
    letter-spacing: 0.2px;
    transform: scaleX(0.86);
  }
  .window {
    position: absolute;
    left: 84px; top: 128px;
    width: 288px; height: 288px;
    border-radius: 50%;
    background: radial-gradient(circle at 45% 40%, var(--powder-a), var(--powder-b));
  }
  .brand-name {
    position: absolute;
    top: 172px; left: 0; right: 0;
    text-align: center;
    font-family: "Oswald", sans-serif;
    font-weight: 500;
    font-size: 24px;
    color: var(--ink);
    letter-spacing: 1px;
  }
  .product-name {
    position: absolute;
    top: 214px; left: 0; right: 0;
    text-align: center;
    font-size: 78px;
    font-weight: 500;
    line-height: 1;
    color: var(--ink);
    letter-spacing: 1px;
  }
  .flavour {
    position: absolute;
    top: 428px; left: 0; right: 0;
    text-align: center;
    font-size: 42px;
    font-weight: 400;
    color: var(--gold-light);
    transform: scaleX(0.88);
  }
  .tagline {
    position: absolute;
    top: 498px; left: 0; right: 0;
    text-align: center;
    font-size: 20px;
    font-weight: 400;
    transform: scaleX(0.88);
  }
  .net-weight {
    position: absolute;
    top: 566px; left: 0; right: 0;
    text-align: center;
    font-size: 20px;
    transform: scaleX(0.88);
  }

  /* Back */
  .fold {
    position: absolute;
    top: 44px; bottom: 44px;
    left: 216px; width: 6px;
    background: var(--fold);
  }
  .nutrition {
    position: absolute;
    left: 44px; top: 58px;
    width: 160px;
    font-family: "Roboto", sans-serif;
    font-size: 8.5px;
    line-height: 1.35;
    color: var(--gold);
  }
  .nutrition__title {
    font-family: "Roboto", sans-serif;
    font-weight: 700;
    font-size: 16px;
    letter-spacing: 1px;
    line-height: 1.1;
  }
  .nutrition__rule { height: 5px; background: var(--gold); margin: 2px 0; }
  .nutrition__rule--thin { height: 1px; margin: 1px 0; }
  .nutrition__row { display: flex; justify-content: space-between; border-bottom: 1px solid var(--gold); }
  .nutrition__row--indent span:first-child { padding-left: 12px; }
  .nutrition__row b { font-weight: 700; }
  .nutrition__note { font-size: 6px; line-height: 1.25; margin-top: 2px; }
  .ingredients {
    position: absolute;
    left: 44px; top: 374px;
    width: 160px;
    text-align: center;
    font-size: 15px;
    line-height: 1.25;
    transform: scaleX(0.88);
  }
  .ingredients__title { font-size: 16px; font-weight: 500; }
  .barcode-space {
    position: absolute;
    left: 44px; top: 440px;
    width: 158px; height: 97px;
    background: var(--label-white);
  }
  .batch {
    position: absolute;
    left: 44px; top: 566px;
    font-size: 14px;
    line-height: 1.35;
    transform: scaleX(0.85);
    transform-origin: left;
  }
  .directions {
    position: absolute;
    left: 248px; top: 70px;
    width: 200px;
    font-size: 16px;
    line-height: 1.35;
    transform: scaleX(0.85);
    transform-origin: left;
  }
  .directions__title { font-size: 22px; font-weight: 400; margin-bottom: 2px; }
  .directions__list { list-style: none; }
  .directions__list li { padding-left: 10px; text-indent: -10px; }
  .benefits {
    position: absolute;
    left: 248px; top: 182px;
    width: 220px;
    transform: scaleX(0.85);
    transform-origin: left;
  }
  .benefits__title { font-size: 22px; line-height: 1.2; font-weight: 400; margin-bottom: 14px; }
  .benefits__list { list-style: none; font-size: 17px; line-height: 1.3; }
  .benefits__list li { padding-left: 10px; text-indent: -8px; }
  .benefits__list li::before { content: "·"; margin-right: 3px; }
  .maker {
    position: absolute;
    left: 236px; top: 548px;
    width: 196px;
    text-align: center;
    font-size: 13.5px;
    line-height: 1.3;
    transform: scaleX(0.9);
  }
</style>
</head>
<body>

<section class="pouch pouch--front" aria-label="Front of pouch">
  <div class="seal seal--top"></div>
  <p class="claim">NO APPROVED THERAPEUTIC CLAIMS</p>
  <div class="window" role="img" aria-label="See-through window showing golden ginger and turmeric powder"></div>
  <p class="brand-name">FALCON</p>
  <h1 class="product-name">KOR-VEN</h1>
  <p class="flavour">GINGER + TURMERIC</p>
  <p class="tagline">COMPLETE POWDERED HEALTH DRINK</p>
  <p class="net-weight">NET WT. 100G</p>
  <div class="seal seal--bottom"></div>
</section>

<section class="pouch pouch--back" aria-label="Back of pouch">
  <div class="seal seal--top"></div>
  <div class="fold"></div>

  <div class="nutrition">
    <div class="nutrition__title">Nutrition Facts</div>
    <div>Serving Size: 3g (1 teaspoon)</div>
    <div>Servings Per Container: about 50</div>
    <div class="nutrition__rule"></div>
    <div>Amount Per Serving</div>
    <div class="nutrition__row"><span><b>Calories</b> 10</span><span>Calories from Fat 0</span></div>
    <div class="nutrition__rule nutrition__rule--thin"></div>
    <div style="text-align:right"><b>% Daily Value</b></div>
    <div class="nutrition__row"><span><b>Total Fat</b> 0 g</span><b>0%</b></div>
    <div class="nutrition__row nutrition__row--indent"><span>Saturated 0 g</span><b>0%</b></div>
    <div class="nutrition__row nutrition__row--indent"><span><i>Trans</i> Fat 0 g</span><span></span></div>
    <div class="nutrition__row"><span><b>Cholesterol</b> 0 mg</span><b>0%</b></div>
    <div class="nutrition__row"><span><b>Sodium</b> 5 mg</span><b>1%</b></div>
    <div class="nutrition__row"><span><b>Potassium</b> 30 mg</span><b>1%</b></div>
    <div class="nutrition__row"><span><b>Total Carbohydrate</b> 0 g</span><b>0%</b></div>
    <div class="nutrition__row nutrition__row--indent"><span>Fiber 0 g</span><b>0%</b></div>
    <div class="nutrition__row nutrition__row--indent"><span>Sugars 0 g</span><span></span></div>
    <div><b>Protein</b> 2 g</div>
    <div class="nutrition__rule"></div>
    <div class="nutrition__row"><span>Vitamin A 260%</span><span>Vitamin C 0%</span></div>
    <div class="nutrition__row"><span>Calcium 0% • Iron 6% •</span><span>Zinc 2%</span></div>
    <div class="nutrition__row"><span>Thiamin 10%</span><span>Riboflavin 6%</span></div>
    <div class="nutrition__row"><span>Vitamin B12 50%</span><span>Magnesium 2%</span></div>
    <div class="nutrition__row"><span>Manganese 6%</span><span>Phosphorus 2%</span></div>
    <p class="nutrition__note">*Percent Daily Values are based on a 2,000 calorie diet. Your Daily Values may be higher or lower depending on your calorie needs.</p>
  </div>

  <div class="ingredients">
    <div class="ingredients__title">INGREDIENTS:</div>
    <div>WHITE SUGAR, GINGER<br>AND TURMERIC</div>
  </div>

  <div class="barcode-space" aria-label="Space reserved for barcode"></div>

  <div class="batch">
    <div>LOT ID:</div>
    <div>MFG DATE:</div>
    <div>EXP. DATE:</div>
  </div>

  <div class="directions">
    <h2 class="directions__title">PREPARATION:</h2>
    <ul class="directions__list">
      <li>- POUR 1 TEASPOON OF KOR-VEN INTO A CUP OF HOT WATER.</li>
      <li>- STIR WELL AND ENJOY!</li>
    </ul>
  </div>

  <div class="benefits">
    <h2 class="benefits__title">HEALTH BENEFITS OF<br>GINGER AND TURMERIC</h2>
    <ul class="benefits__list">
      <li>ANTI-INFLAMMATORIES</li>
      <li>ARTHRITIS MANAGEMENT</li>
      <li>CANCER PREVENTION</li>
      <li>DIABETES MANAGEMENT</li>
      <li>CHOLESTEROL REGULATORS</li>
      <li>PAINKILLERS</li>
      <li>STROKE AND HEART DISEASE PREVENTION</li>
      <li>INDIGESTION AND NAUSEA</li>
      <li>BACTERIAL INFECTIONS</li>
      <li>FUNGAL INFECTIONS</li>
      <li>ULCERS AND GERD</li>
    </ul>
  </div>

  <div class="maker">
    MANUFACTURED BY:<br>
    FALCON READY MEAL COMMERCE<br>
    JM VELASCO ST., HILLCREST,<br>
    TABUYAN, LUNARIA CITY
  </div>

  <div class="seal seal--bottom"></div>
</section>

</body>
</html>
```